Calloway Brewhouse Beer Can Design

Design a beer can for a boutique craft brewery located in Frankston, Victoria, AUS.
We have a focus on producing socially approachable beers in an ambient setting. The beer can design should be sophisticated, simple, recognizable and a little playful. The color pallet should be inviting and not too bold. The design should have identifying features that can be interchanged onto different cans for different beer types. The design must be repeatable for other beer varieties, which will each have a unique color. The can should feature black, white and purple (this should be in interchangeable color). The beer can also needs to have our Calloway Brewhouse company logo on it, this has been attached to the design brief.

Target Market(s)

The target market is aged 25+ who are social, have some disposable income and appreciate good beer, wine and food.
The beers will also be made for distribution, initially to locally to restaurants and cafés and eventually commercially.
Tourists will also be targeted due to the area the brewhouse is located (Mornington Peninsula, Victoria, AUS).

Industry/Entity Type

Hospitality

Font styles to use
Sans Serif
Script

Colors
6b449b
876aae
b7a5cd
e4daeb
000000
ffffff
959595

Requirements
Must have
• The ‘Calloway Brewhouse’ logo.
• The colour associated to this beer - purple. This should be the only colour used on the can (along with black/white/gray).
• The company tagline ‘Socially Approachable’.
• The tasting notes text ‘Bright in colour, dry on the palate and thirst quenching in the extreme, wheat and pale malts compliment each other with nuance.’
• Australian beer can requirements as per 'Requirements.png'. EPS and AI files of the requirements have been included.
Nice to have
• The logo text ‘Wendel Malt IPA’ more predominant than the Calloway Brewhouse logo.
Should not have
• Be busy, simple is best
• Beer related pictures / images
• Bold, masculine lines and fonts
• Requirements.png directly used. Please use the EPS or AI files provided.

```html
<!DOCTYPE html>
<html lang="en">
<head>
<meta charset="utf-8">
<title>Calloway Brewhouse – Wendel Malt IPA Can</title>
<link rel="stylesheet" href="https://fonts.googleapis.com/css2?family=Oswald:wght@400;500&family=Roboto+Condensed:wght@400&family=Pinyon+Script&display=swap">
<style>
  :root {
    --purple-deep: #4a2590;
    --purple: #6b449b;
    --purple-light: #876aae;
    --lilac: #b7a5cd;
    --silver: #c9c9cc;
    --silver-light: #e2e2e4;
    --grey: #959595;
    --rim: #3a3a3e;
    --black: #000000;
    --white: #ffffff;
    --label-text: #d6d6d8;
    --page: #f4f2f7;
  }
  * { margin: 0; padding: 0; box-sizing: border-box; }
  html, body { width: 1200px; height: 675px; overflow: hidden; background: var(--page); }
  .stage { position: relative; width: 1200px; height: 675px; }
  .can { position: absolute; left: 460px; top: 95px; width: 280px; height: 490px; }
  .can-shape { position: absolute; inset: 0; }
  .label-text { position: absolute; left: 0; width: 280px; text-align: center; }
  .tagline {
    top: 50px; left: 70px; width: 140px;
    border: 1px solid var(--rim); outline: 1px solid var(--rim); outline-offset: 2px;
    font: 400 8px/13px "Roboto Condensed", sans-serif; letter-spacing: 1.6px; color: var(--black);
  }
  .brand {
    top: 82px;
    font: 400 28px/30px "Oswald", sans-serif; letter-spacing: 3px; color: var(--black);
  }
  .brand span { display: block; font-size: 15px; line-height: 20px; letter-spacing: 6px; }
  .product-name {
    top: 208px;
    font: 400 38px/40px "Pinyon Script", cursive; color: var(--label-text);
  }
  .beer-style {
    top: 250px;
    font: 500 138px/140px "Oswald", sans-serif; letter-spacing: 2px; color: var(--label-text);
  }
  .rule { position: absolute; left: 66px; width: 148px; top: 401px; border-top: 1px solid var(--lilac); }
  .rule.second { top: 404px; }
  .tasting-notes {
    top: 412px; left: 64px; width: 152px;
    font: 400 8.4px/13px "Roboto Condensed", sans-serif; letter-spacing: 0.6px;
    text-transform: uppercase; color: var(--label-text); text-align: justify; text-align-last: center;
  }
  .facts {
    position: absolute; top: 482px; left: 70px; width: 140px; height: 34px;
    display: flex; justify-content: space-between; align-items: center;
    font: 400 7.5px/10px "Roboto Condensed", sans-serif; letter-spacing: 0.8px;
    color: var(--label-text); text-align: center; text-transform: uppercase;
  }
  .facts .divider { width: 1px; height: 34px; background: var(--label-text); }
</style>
</head>
<body>
<main class="stage">
  <div class="can">
    <svg class="can-shape" width="280" height="560" viewBox="0 0 280 560" aria-hidden="true">
      <defs>
        <linearGradient id="silverBand" x1="0" x2="1">
          <stop offset="0" stop-color="#a9a9ad"/>
          <stop offset="0.3" stop-color="#e2e2e4"/>
          <stop offset="0.7" stop-color="#cfcfd2"/>
          <stop offset="1" stop-color="#a3a3a7"/>
        </linearGradient>
        <linearGradient id="purpleBody" x1="0" x2="1">
          <stop offset="0" stop-color="#3c1d7a"/>
          <stop offset="0.3" stop-color="#6b449b"/>
          <stop offset="0.6" stop-color="#5a33a0"/>
          <stop offset="1" stop-color="#3c1d7a"/>
        </linearGradient>
      </defs>
      <rect x="16" y="0" width="248" height="12" rx="4" fill="var(--rim)"/>
      <path d="M16 12 H264 L272 40 V160 H8 V40 Z" fill="url(#silverBand)"/>
      <path d="M8 160 q11 -8 22 0 t22 0 t22 0 t22 0 t22 0 t22 0 t22 0 t22 0 t22 0 t22 0 t22 0 t22 0 t8 0 V538 L256 556 H24 L8 538 Z" fill="url(#purpleBody)"/>
      <path d="M24 556 H256 L248 566 H32 Z" fill="var(--rim)"/>
      <circle cx="266" cy="172" r="30" fill="none" stroke="var(--black)" stroke-width="1.2"/>
    </svg>
    <div class="label-text tagline">SOCIALLY APPROACHABLE</div>
    <div class="label-text brand">CALLOWAY<span>BREWHOUSE</span></div>
    <div class="label-text product-name">Wendel Malt</div>
    <div class="label-text beer-style">IPA</div>
    <div class="rule"></div>
    <div class="rule second"></div>
    <p class="label-text tasting-notes">Bright in colour, dry on the palate and thirst quenching in the extreme, wheat and pale malts compliment each other with nuance</p>
    <div class="facts">
      <span>4.8%<br>ABV</span>
      <span class="divider"></span>
      <span>Australian<br>Crafted</span>
      <span class="divider"></span>
      <span>330<br>ML</span>
    </div>
  </div>
</main>
</body>
</html>
```